Pine Hollow Canine Massage Needs a Business Card Design

Pine Hollow Canine Massage is a new therapeutic canine massage company located in Nederland, Colorado. I need a business card design that include my logo and basic contact information.

Target Market(s)

Pet owners, veterinarians

Industry/Entity Type

Business

Contact Information for Business Card

Linda Morrow, CCMT
303.518.7290
linda@pinehollowmassage.example
www.pinehollowmassage.example

Colors
6c459b
886aae
b8a6cd
a64599
b768aa
d3a5cc
fbed22

Requirements
Must have
• Font should be similar to font in logo.

```html
<!DOCTYPE html>
<html lang="en">
<head>
<meta charset="utf-8">
<title>Pine Hollow Canine Massage – Business Card</title>
<link rel="stylesheet" href="https://fonts.googleapis.com/css2?family=Open+Sans:wght@400;600;700&display=swap">
<style>
  :root {
    --stage: #ecebee;
    --lilac: #b581bd;
    --plum-deep: #3f1a55;
    --plum-mid: #552a72;
    --ink-purple: #5a2d78;
    --gold: #f2c83a;
    --white: #ffffff;
    --hill-faint: #f3f1f5;
    --card-shadow: rgba(40, 20, 60, 0.22);
  }
  * { box-sizing: border-box; margin: 0; padding: 0; }
  html, body {
    width: 1200px; height: 900px; overflow: hidden;
    background: var(--stage);
    font-family: "Open Sans", Arial, sans-serif;
  }
  .stage { position: relative; width: 1200px; height: 900px; }

  .card {
    position: absolute; width: 560px; height: 340px;
    overflow: hidden; box-shadow: 0 8px 24px var(--card-shadow);
  }

  /* Front */
  .card-front { left: 110px; top: 80px; background: var(--lilac); }
  .card-front .hill { position: absolute; inset: 0; }
  .brand-ring {
    position: absolute; left: 14px; top: 42px; width: 256px; height: 256px;
    border: 4px solid var(--gold); border-radius: 50%;
  }
  .brand-name {
    position: absolute; left: 14px; top: 42px; width: 256px; height: 256px;
    padding-top: 84px;
    display: flex; flex-direction: column; align-items: center; justify-content: center;
    color: var(--gold); font-weight: 700; font-size: 20px; line-height: 1.3;
    letter-spacing: 0.5px; text-align: center; text-transform: uppercase;
  }
  .brand-name span { display: block; }
  .contact {
    position: absolute; right: 24px; top: 70px; text-align: right; color: var(--white);
  }
  .contact-name { font-weight: 700; font-size: 19px; margin-bottom: 22px; }
  .contact-name small { font-size: 13px; font-weight: 600; }
  .contact-line {
    display: flex; justify-content: flex-end; align-items: center; gap: 6px;
    font-size: 13px; line-height: 24px;
  }
  .contact-line svg { width: 12px; height: 12px; fill: var(--white); }

  /* Back */
  .card-back { left: 530px; top: 480px; background: var(--white); color: var(--ink-purple); }
  .card-back .hill { position: absolute; inset: 0; }
  .appt-title {
    position: absolute; top: 44px; width: 100%; text-align: center;
    font-size: 21px; font-weight: 600;
  }
  .appt-fields {
    position: absolute; top: 132px; width: 100%; text-align: center; font-size: 15px;
  }
  .appt-fields b { font-weight: 600; }
  .blank { letter-spacing: 1px; }
  .appt-days {
    position: absolute; top: 200px; width: 100%;
    display: flex; justify-content: center; gap: 20px; font-size: 14px;
  }
  .day { display: flex; align-items: center; gap: 5px; }
  .box { width: 19px; height: 19px; border: 2px solid var(--ink-purple); }
  .appt-note {
    position: absolute; top: 266px; width: 100%; text-align: center;
    font-size: 15px; font-weight: 600; line-height: 1.3;
  }
</style>
</head>
<body>
<main class="stage">

  <section class="card card-front">
    <svg class="hill" width="560" height="340" viewBox="0 0 560 340" aria-hidden="true">
      <defs>
        <linearGradient id="hillShade" x1="0" y1="0" x2="0" y2="1">
          <stop offset="0" stop-color="var(--plum-mid)"/>
          <stop offset="1" stop-color="var(--plum-deep)"/>
        </linearGradient>
      </defs>
      <path d="M0,200 C90,170 260,185 560,335 L560,340 L0,340 Z" fill="url(#hillShade)"/>
    </svg>
    <div class="brand-ring"></div>
    <div class="brand-name"><span>Pine Hollow</span><span>Canine Massage</span></div>

    <div class="contact">
      <p class="contact-name">Linda Morrow, <small>CCMT</small></p>
      <p class="contact-line">303.518.7290
        <svg viewBox="0 0 24 24"><path d="M6.6 10.8a15.1 15.1 0 0 0 6.6 6.6l2.2-2.2a1 1 0 0 1 1-.25 11.4 11.4 0 0 0 3.6.6 1 1 0 0 1 1 1V20a1 1 0 0 1-1 1A17 17 0 0 1 3 4a1 1 0 0 1 1-1h3.5a1 1 0 0 1 1 1c0 1.25.2 2.45.6 3.6a1 1 0 0 1-.25 1z"/></svg>
      </p>
      <p class="contact-line">linda@pinehollowmassage.example
        <svg viewBox="0 0 24 24"><path d="M2 5h20v14H2z M3 6l9 7 9-7" stroke="var(--lilac)" stroke-width="1.5"/></svg>
      </p>
      <p class="contact-line">www.pinehollowmassage.example
        <svg viewBox="0 0 24 24"><circle cx="12" cy="12" r="10"/><path d="M2 12h20M12 2c3 3 3 17 0 20M12 2c-3 3-3 17 0 20" stroke="var(--lilac)" stroke-width="1.4" fill="none"/></svg>
      </p>
    </div>
  </section>

  <section class="card card-back">
    <svg class="hill" width="560" height="340" viewBox="0 0 560 340" aria-hidden="true">
      <path d="M0,330 C150,300 330,300 480,340 L0,340 Z" fill="var(--hill-faint)"/>
    </svg>
    <h2 class="appt-title">Your Next Appointment on</h2>
    <p class="appt-fields">
      <b>Date :</b> <span class="blank">.............................</span>
      &nbsp;<b>Time :</b> <span class="blank">............................</span> AM / PM
    </p>
    <div class="appt-days">
      <span class="day"><span class="box"></span>MON</span>
      <span class="day"><span class="box"></span>TUE</span>
      <span class="day"><span class="box"></span>WED</span>
      <span class="day"><span class="box"></span>THU</span>
      <span class="day"><span class="box"></span>FRI</span>
      <span class="day"><span class="box"></span>SAT</span>
    </div>
    <p class="appt-note">If unable to keep appointment,<br>kindly give 24hrs notice.</p>
  </section>

</main>
</body>
</html>
```